Agriculture farming Hemp and CBD

The logo is in works with your company now, should be ready in a few days. We have our Domain (thequillmarkfarms.com) We would like to see incorporated seed to growth, but not necessary. we would like to nature colors and some black and green. we have our farm and will be growing and selling HEMP and CBD we are based in the state of Virginia. Would like to incorporate the words pause, play, rewind if possible but not necessary.

Target Market(s)

20 years old to elderly

Coding

Coded - Design and coding required

Number of Pages Required

3 page

Font styles to use
Serif

Requirements
Must have
• I'm not sure on the must haves, we are open to any ideas, we would definitely like to see Hemp and CBD included, may the life cycle of seed to plant. We must have a pop up asking if you are 20 years old before they can enter our site and to view or purchase our product. I want the design to be totally different than what i uploaded.
Nice to have
• Would like to see natural colors as well as black and green
Should not have
• I want

```html
<!DOCTYPE html>
<html lang="en">
<head>
<meta charset="utf-8">
<title>Quillmark Farms – Hemp &amp; CBD</title>
<link href="https://fonts.googleapis.com/css2?family=Josefin+Sans:wght@400;600;700&family=Montserrat:ital,wght@0,400;0,500;0,600;0,700;1,400&display=swap" rel="stylesheet">
<style>
:root{
  --green:#3f9a1e;
  --green-bright:#4aa822;
  --green-dark:#2b6f12;
  --brown:#5b3611;
  --brown-dark:#43270b;
  --tan:#f4ddb0;
  --black:#0d0d0d;
  --ink:#1c1c1c;
  --muted:#8d8d8d;
  --beige:#ece3d8;
  --white:#ffffff;
  --head:'Josefin Sans',sans-serif;
  --body:'Montserrat',sans-serif;
}
*{box-sizing:border-box;margin:0;padding:0}
html,body{width:1200px;height:4880px;overflow:hidden}
body{position:relative;font-family:var(--body);color:var(--ink);background:var(--white)}
.abs{position:absolute}
.btn{position:absolute;display:flex;align-items:center;justify-content:center;font-family:var(--body);font-weight:700;font-size:11px;letter-spacing:.5px;border-radius:30px;text-transform:uppercase}
.btn-outline{border:2px solid var(--brown);color:var(--brown);background:transparent}
.btn-tan{background:var(--tan);color:var(--brown)}
.btn-green{background:var(--green-dark);color:var(--white)}

/* header */
.site-header{position:absolute;left:0;top:0;width:1200px;height:92px;background:var(--black);z-index:5}
.brand{position:absolute;font-family:var(--head);font-weight:700;color:var(--white);white-space:nowrap}
.site-header .brand{left:45px;top:26px;font-size:34px}
.nav a{position:absolute;top:42px;font-size:12px;color:var(--white);text-decoration:none;font-weight:500;letter-spacing:.3px}
.nav a.active{color:var(--green-bright)}
.nav .dot{position:absolute;left:496px;top:24px;width:10px;height:10px;border:2px solid var(--white);border-radius:50%}

/* hero */
.hero{position:absolute;left:0;top:92px;width:1200px;height:690px;overflow:hidden}
.hero-photo{position:absolute;inset:0;background:radial-gradient(ellipse at 62% 40%,#6d7a3a 0%,#3a3a20 35%,#2a1d12 65%,#1a120b 100%)}
.hero-badge{position:absolute;left:109px;top:96px;width:388px;height:388px;border-radius:50%;background:radial-gradient(circle at 40% 40%,#4cae24,#2e8414);text-align:center;color:var(--white)}
.hero-badge .pre{margin-top:100px;font-family:var(--head);font-size:28px}
.hero-badge h1{font-family:var(--head);font-weight:700;font-size:46px;line-height:52px;margin-top:6px}
.hero-badge .btn{left:112px;top:250px;width:170px;height:46px;background:var(--brown);color:var(--white);font-size:12px}
.hero-dots span{position:absolute;top:580px;width:11px;height:11px;border-radius:50%;border:2px solid var(--white)}
.hero-dots span.on{background:var(--white)}
.hero-wave{position:absolute;left:0;top:570px;width:1200px;height:220px}

/* about */
.eyebrow{font-family:var(--head);font-size:22px;color:var(--ink)}
.section-title{font-family:var(--head);font-weight:700;font-size:36px;color:var(--black)}
.about .eyebrow{position:absolute;left:137px;top:905px;color:var(--green)}
.about .section-title{position:absolute;left:137px;top:938px}
.about p{position:absolute;left:139px;top:1005px;width:400px;font-size:10.5px;line-height:23px;color:var(--muted)}
.about .btn{left:137px;top:1167px;width:148px;height:42px}
.about-art{position:absolute;left:645px;top:796px;width:380px;height:436px;border-radius:50%}
.features{position:absolute;left:91px;top:1295px;width:1003px;height:122px;border:2px solid #e6e6e6;border-radius:60px;background:var(--white)}
.feature{position:absolute;top:30px;display:flex;align-items:center;gap:18px}
.feature .ico{width:62px;height:62px;border-radius:50%;border:2px solid var(--green);box-shadow:0 0 0 6px #eef6ea}
.feature span{font-size:13px;font-weight:600;line-height:16px;color:var(--ink)}
.features .sep{position:absolute;top:36px;width:1px;height:50px;background:#d8d8d8}

/* products */
.products{position:absolute;left:0;top:1483px;width:1200px;height:437px;background:var(--beige)}
.center-head{position:absolute;left:0;width:1200px;text-align:center}
.products .eyebrow{top:70px}
.products .section-title{top:100px}
.rule{position:absolute;left:568px;width:64px;height:4px;background:var(--green)}
.product-card{position:absolute;top:1691px;width:497px;height:319px;border-radius:34px;overflow:hidden;color:var(--white)}
.product-card .photo{position:absolute;inset:0}
.product-card h3{position:absolute;left:47px;top:76px;font-family:var(--head);font-weight:700;font-size:34px}
.product-card p{position:absolute;left:48px;top:120px;width:230px;font-size:11px;line-height:20px}
.product-card .btn{left:48px;top:198px;width:116px;height:30px;font-size:9.5px}
.controls{position:absolute;left:52px;top:255px}
.why-photo{position:absolute;left:0;top:2010px;width:650px;height:720px}
.why .eyebrow{position:absolute;left:655px;top:2138px}
.why .section-title{position:absolute;left:655px;top:2176px}
.why .rule{left:657px;top:2230px;width:62px}
.why-item{position:absolute;left:655px;width:470px}
.why-item svg{position:absolute;left:5px;top:0}
.why-item h4{position:absolute;left:98px;top:0;font-size:15px;font-weight:500;color:var(--ink)}
.why-item p{position:absolute;left:98px;top:24px;width:360px;font-size:11px;line-height:19px;color:var(--muted)}
.why .btn{left:651px;top:2578px;width:146px;height:40px}

/* testimonials */
.testimonials{position:absolute;left:0;top:2730px;width:1200px;height:526px;background:linear-gradient(180deg,#46a421,#3a9a18)}
.testimonials .section-title{top:58px;color:var(--white)}
.testimonials .rule{top:104px;background:var(--white)}
.quote{position:absolute;top:129px;width:312px;height:312px;border-radius:50%;border:2px solid rgba(255,255,255,.8);padding:12px}
.quote .inner{width:100%;height:100%;border-radius:50%;text-align:center;color:var(--white);padding-top:38px}
.quote .mark{font-family:Georgia,serif;font-size:70px;line-height:40px;color:rgba(255,255,255,.45);height:42px}
.quote p{width:210px;margin:16px auto 0;font-style:italic;font-size:10.5px;line-height:20px}
.quote h5{margin-top:14px;font-size:12px;font-weight:700}
.stars{margin-top:4px;color:#f5c518;font-size:17px;letter-spacing:2px}
.arrow{position:absolute;top:261px;width:28px;height:28px;border-radius:50%;background:var(--white);display:flex;align-items:center;justify-content:center}

/* blog */
.blog{position:absolute;left:0;top:3256px;width:1200px;height:626px;background:#efe9e1}
.blog .eyebrow{top:52px;font-size:20px}
.blog .section-title{top:82px}
.blog .rule{top:124px}
.post{position:absolute;top:3409px;width:297px;height:391px;background:var(--white);box-shadow:0 4px 14px rgba(0,0,0,.08)}
.post .photo{position:absolute;left:0;top:0;width:100%;height:218px}
.post .date{position:absolute;left:0;top:144px;width:66px;height:74px;background:var(--brown);color:var(--white);text-align:center;padding-top:10px}
.post .date b{display:block;font-family:var(--head);font-size:30px;line-height:30px}
.post .date small{font-size:12px}
.post h4{position:absolute;left:20px;top:240px;width:260px;font-size:13.5px;line-height:18px;font-weight:700}
.post p{position:absolute;left:20px;top:290px;width:260px;font-size:9px;line-height:13px;color:var(--muted)}
.post .btn{left:20px;top:337px;width:112px;height:32px;font-size:9px}

/* contact */
.contact{position:absolute;left:0;top:3882px;width:1200px;height:612px;overflow:hidden}
.contact-photo{position:absolute;left:0;top:0;width:1200px;height:612px;background:linear-gradient(90deg,#a7782c 0%,#6a6024 25%,#5a4214 48%,var(--brown) 55%,var(--brown) 100%)}
.contact .eyebrow{position:absolute;left:643px;top:78px;color:var(--white)}
.contact .section-title{position:absolute;left:643px;top:108px;color:var(--white)}
.field{position:absolute;left:645px;width:428px;height:46px;background:var(--white);font-size:12px;color:#555;padding:14px 18px}
.contact .btn{left:643px;top:441px;width:140px;height:40px;font-size:12px}
.contact-wave{position:absolute;left:0;top:4350px;width:1200px;height:150px}

/* footer */
.site-footer{position:absolute;left:0;top:4493px;width:1200px;height:387px;background:var(--black);color:var(--white)}
.site-footer .brand{left:104px;top:62px;font-size:30px}
.contact-line{position:absolute;left:104px;display:flex;gap:12px;font-size:13px;line-height:19px}
.foot-col{position:absolute;top:64px}
.foot-col h6{font-size:16px;font-weight:600;margin-bottom:14px}
.foot-col a{display:block;font-size:10.5px;color:#e6e6e6;text-decoration:none;line-height:29px}
.newsletter-input{position:absolute;left:876px;top:101px;width:237px;height:35px;background:#e6e6e6;color:#888;font-size:11px;padding:10px 14px}
.site-footer .btn{left:876px;top:150px;width:112px;height:32px;font-size:9.5px}
.social{position:absolute;top:207px;width:28px;height:28px;border-radius:50%;background:var(--green)}
.foot-rule{position:absolute;left:0;top:320px;width:1200px;height:1px;background:#2a2a2a}
.copyright{position:absolute;top:343px;font-size:10px;color:#cfcfcf}
</style>
</head>
<body>

<header class="site-header">
  <div class="brand">thequillmarkfarms.com</div>
  <nav class="nav">
    <span class="dot"></span>
    <a class="active" style="left:481px">HOME</a>
    <a style="left:566px">ABOUT US</a>
    <a style="left:675px">PRODUCTS</a>
    <a style="left:789px">SHOP</a>
    <a style="left:870px">BLOGS</a>
    <a style="left:957px">TESTIMONIALS</a>
    <a style="left:1092px">CONTACT</a>
  </nav>
</header>

<section class="hero">
  <div class="hero-photo" role="img" aria-label="Close-up photo of dried hemp flower buds on a dark wooden board"></div>
  <div class="hero-badge">
    <div class="pre">Specialize in</div>
    <h1>Selling Quality<br>Hemp &amp; CBD</h1>
    <a class="btn">Contact us &rsaquo;</a>
  </div>
  <div class="hero-dots">
    <span class="on" style="left:575px"></span><span style="left:602px"></span><span style="left:628px"></span>
  </div>
  <svg class="hero-wave" viewBox="0 0 1200 220" preserveAspectRatio="none">
    <path d="M0 150 C250 60 500 40 760 70 C950 90 1100 130 1200 205 L1200 220 L0 220Z" fill="#5b3611"/>
    <path d="M0 140 C240 40 520 20 780 55 C960 80 1100 120 1200 185 L1200 220 L0 220Z" fill="#3f9a1e"/>
    <path d="M0 175 C260 90 520 75 780 95 C960 110 1100 150 1200 220 L0 220Z" fill="#5b3611"/>
    <path d="M0 190 C260 110 520 95 780 115 C960 130 1100 170 1200 220 L0 220Z" fill="#ffffff"/>
  </svg>
</section>

<section class="about">
  <div class="eyebrow">Who We Are</div>
  <h2 class="section-title">About Quillmark Farms</h2>
  <p>Curabitur vel dolor ultrices ipsum dictum tristique Praesent vitae lacus Ut velit enim vestibulum non fermentum nec hendrerit quis leo Pellentesque rutrum malesuada neque Nunc tempus felis vitae urna Vivamus porttitor neque at volutpat rutrum purus nisi eleifend libero a tempus Morbi diam mauris viverra in gravida eu mattis in anquam Curabitur vel dolor ultrices ipsum dictum tristique Praesent vitae lacus Ut velit enim</p>
  <a class="btn btn-outline">Learn more &rsaquo;</a>
  <div class="about-art" role="img" aria-label="Illustration of hemp growing from seed to potted plant in a circle around a leaf-filled power symbol" style="background:radial-gradient(circle,#5ea03a 0 22%,#ffffff 23% 70%,#eef3e8 71% 100%)"></div>

  <div class="features">
    <div class="feature" style="left:46px"><div class="ico"></div><span>GLUTEN<br>FREE</span></div>
    <div class="sep" style="left:247px"></div>
    <div class="feature" style="left:282px"><div class="ico"></div><span>VEGAN</span></div>
    <div class="sep" style="left:458px"></div>
    <div class="feature" style="left:494px"><div class="ico"></div><span>NO GMO 3RD<br>PARTY TESTED</span></div>
    <div class="sep" style="left:730px"></div>
    <div class="feature" style="left:766px"><div class="ico"></div><span>FARM BILL<br>COMPLIANT</span></div>
  </div>
</section>

<section class="products">
  <div class="eyebrow center-head" style="top:70px">Product &amp; Service</div>
  <h2 class="section-title center-head" style="top:100px">What We Group &amp; Selling</h2>
  <div class="rule" style="top:152px"></div>
</section>

<div class="why-photo" role="img" aria-label="Photo of CBD oil dropper bottles on a white plate with hemp leaves" style="background:linear-gradient(120deg,#dfe4dc 0%,#eceeea 40%,#c9d2b8 70%,#f4f4f2 100%)"></div>

<article class="product-card" style="left:99px">
  <div class="photo" role="img" aria-label="Photo of hemp seeds, hemp powder and hemp oil in a glass jar" style="background:linear-gradient(90deg,#2f7f18 0%,#3c8a22 45%,#6b6a33 70%,#8a6d3a 100%)"></div>
  <h3>HEMP</h3>
  <p>Aa eu mattis in anquam Curabitur vel dolor ultrices ipsum dictum tristique Praesent vitae lacus velit enim</p>
  <a class="btn btn-tan">Shop now &rsaquo;</a>
  <svg class="controls" width="100" height="20" viewBox="0 0 100 20" aria-label="rewind, play, pause"><path d="M9 4 L1 10 L9 16Z M17 4 L9 10 L17 16Z" fill="#fff"/><path d="M40 4 L50 10 L40 16Z" fill="#fff"/><rect x="72" y="4" width="4" height="12" fill="#fff"/><rect x="79" y="4" width="4" height="12" fill="#fff"/></svg>
</article>

<article class="product-card" style="left:612px">
  <div class="photo" role="img" aria-label="Photo of CBD oil dropper bottles with hemp leaves on a light surface" style="background:linear-gradient(90deg,#3e2510 0%,#5b3611 40%,#b8a690 75%,#e9e6e0 100%)"></div>
  <h3 style="left:55px">CBD</h3>
  <p style="left:56px">Aa eu mattis in anquam Curabitur vel dolor ultrices ipsum dictum tristique Praesent vitae lacus velit enim</p>
  <a class="btn btn-tan" style="left:56px;top:203px">Shop now &rsaquo;</a>
  <svg class="controls" style="left:58px" width="100" height="20" viewBox="0 0 100 20" aria-label="rewind, play, pause"><path d="M9 4 L1 10 L9 16Z M17 4 L9 10 L17 16Z" fill="#fff"/><path d="M40 4 L50 10 L40 16Z" fill="#fff"/><rect x="72" y="4" width="4" height="12" fill="#fff"/><rect x="79" y="4" width="4" height="12" fill="#fff"/></svg>
</article>

<section class="why">
  <div class="eyebrow">Why Choose Us</div>
  <h2 class="section-title">Why Our Products</h2>
  <div class="rule"></div>
  <div class="why-item" style="top:2283px">
    <svg width="56" height="50" viewBox="0 0 56 50"><path d="M28 45 V10 M28 30 L12 18 M28 30 L44 18 M28 38 L8 32 M28 38 L48 32" stroke="#3f9a1e" stroke-width="2.5" fill="none" stroke-linecap="round"/></svg>
    <h4>100% Natural</h4>
    <p>Aa eu mattis in anquam Curabitur vel dolor ultrices ipsum dictum tristique Praesent vitae lacus velit enim</p>
  </div>
  <div class="why-item" style="top:2387px">
    <svg width="56" height="50" viewBox="0 0 56 50"><path d="M28 44 C10 32 4 22 8 14 C12 6 22 6 28 15 C34 6 44 6 48 14 C52 22 46 32 28 44Z" stroke="#3f9a1e" stroke-width="2.5" fill="none"/><path d="M6 26 H18 L22 18 L28 34 L32 24 H50" stroke="#3f9a1e" stroke-width="2.5" fill="none"/></svg>
    <h4>Health Benefits</h4>
    <p>Aa eu mattis in anquam Curabitur vel dolor ultrices ipsum dictum tristique Praesent vitae lacus velit enim</p>
  </div>
  <div class="why-item" style="top:2483px">
    <svg width="56" height="50" viewBox="0 0 56 50"><rect x="8" y="8" width="40" height="32" stroke="#3f9a1e" stroke-width="2.5" fill="none"/><path d="M28 40 V16 M28 26 L18 20 M28 26 L38 20" stroke="#3f9a1e" stroke-width="2.5" fill="none"/></svg>
    <h4>Experienced</h4>
    <p>Aa eu mattis in anquam Curabitur vel dolor ultrices ipsum dictum tristique Praesent vitae lacus velit enim</p>
  </div>
  <a class="btn btn-outline">Learn more &rsaquo;</a>
</section>

<section class="testimonials">
  <h2 class="section-title center-head">Testimonials</h2>
  <div class="rule"></div>
  <div class="arrow" style="left:77px"><svg width="10" height="10" viewBox="0 0 10 10"><path d="M7 1 L3 5 L7 9" stroke="#3f9a1e" stroke-width="2" fill="none"/></svg></div>
  <div class="arrow" style="left:1116px"><svg width="10" height="10" viewBox="0 0 10 10"><path d="M3 1 L7 5 L3 9" stroke="#3f9a1e" stroke-width="2" fill="none"/></svg></div>

  <div class="quote" style="left:121px"><div class="inner" style="background:#2d7b14">
    <div class="mark">&ldquo;</div>
    <p>Aultrices orci ac feugiat suscipit leo massa sodales velit et scelerisque mi tortor at ipsum Proin orci odio commodo ac gravida non tristique vel te Curabitur iaculis tempus eros</p>
    <h5>Nora Ellis</h5><div class="stars">★★★★★</div>
  </div></div>
  <div class="quote" style="left:447px"><div class="inner" style="background:var(--brown)">
    <div class="mark">&ldquo;</div>
    <p>Aultrices orci ac feugiat suscipit leo massa sodales velit et scelerisque mi tortor at ipsum Proin orci odio commodo ac gravida non tristique vel te Curabitur iaculis tempus eros</p>
    <h5>Nora Ellis</h5><div class="stars">★★★★★</div>
  </div></div>
  <div class="quote" style="left:767px"><div class="inner" style="background:#2d7b14">
    <div class="mark">&ldquo;</div>
    <p>Aultrices orci ac feugiat suscipit leo massa sodales velit et scelerisque mi tortor at ipsum Proin orci odio commodo ac gravida non tristique vel te Curabitur iaculis tempus eros</p>
    <h5>Nora Ellis</h5><div class="stars">★★★★★</div>
  </div></div>
</section>

<section class="blog">
  <div class="eyebrow center-head">Articles &amp; News</div>
  <h2 class="section-title center-head">Recent Blog</h2>
  <div class="rule"></div>
</section>

<article class="post" style="left:144px">
  <div class="photo" role="img" aria-label="Photo of a green hemp leaf" style="background:linear-gradient(160deg,#9bc46a,#3f7f22 60%,#2a5a16)"></div>
  <div class="date"><b>31</b><small>AUG</small></div>
  <h4>Morbi diam mauris viverra in gravida eu mattis in</h4>
  <p>Praesent vitae lacus Ut velit enim vestibulum non fermentum nec hendrerit quis leo Pellentesque rutrum malesuada neque Nunc tempus felis vitae urna</p>
  <a class="btn btn-green">Read more</a>
</article>
<article class="post" style="left:471px">
  <div class="photo" role="img" aria-label="Photo of CBD oil bottles and a honey jar beside hemp leaves" style="background:linear-gradient(160deg,#b9d48a,#7fae3e 50%,#d6b34a)"></div>
  <div class="date"><b>29</b><small>AUG</small></div>
  <h4>Morbi diam mauris viverra in gravida eu mattis in</h4>
  <p>Praesent vitae lacus Ut velit enim vestibulum non fermentum nec hendrerit quis leo Pellentesque rutrum malesuada neque Nunc tempus felis vitae urna</p>
  <a class="btn btn-green">Read more</a>
</article>
<article class="post" style="left:807px">
  <div class="photo" role="img" aria-label="Photo of CBD cream, oil bottle and hemp leaves on a green plate" style="background:linear-gradient(160deg,#e8e4dc,#a9c290 50%,#e2d2b4)"></div>
  <div class="date"><b>31</b><small>AUG</small></div>
  <h4>Morbi diam mauris viverra in gravida eu mattis in</h4>
  <p>Praesent vitae lacus Ut velit enim vestibulum non fermentum nec hendrerit quis leo Pellentesque rutrum malesuada neque Nunc tempus felis vitae urna</p>
  <a class="btn btn-green">Read more</a>
</article>

<section class="contact">
  <div class="contact-photo" role="img" aria-label="Photo of a hemp field at sunset"></div>
  <div class="eyebrow">Contact Form</div>
  <h2 class="section-title">Get in touch with us</h2>
  <div class="field" style="top:170px">Name*</div>
  <div class="field" style="top:225px">Email *</div>
  <div class="field" style="top:280px">Phone*</div>
  <div class="field" style="top:337px;height:82px">Message</div>
  <a class="btn btn-tan">Send &rsaquo;</a>
</section>
<svg class="contact-wave" viewBox="0 0 1200 150" preserveAspectRatio="none">
  <path d="M0 60 C250 20 600 10 900 30 C1050 40 1150 70 1200 90 L1200 150 L0 150Z" fill="#5b3611"/>
  <path d="M0 75 C250 35 600 28 900 48 C1050 58 1150 88 1200 110 L1200 150 L0 150Z" fill="#3f9a1e"/>
  <path d="M0 100 C250 65 600 60 900 78 C1050 88 1150 115 1200 135 L1200 150 L0 150Z" fill="#0d0d0d"/>
</svg>

<footer class="site-footer">
  <div class="brand">thequillmarkfarms.com</div>
  <div class="contact-line" style="top:128px"><svg width="14" height="18" viewBox="0 0 14 18"><path d="M7 17 C2 10 1 8 1 6 A6 6 0 0 1 13 6 C13 8 12 10 7 17Z" fill="#3f9a1e"/><circle cx="7" cy="6" r="2.2" fill="#0d0d0d"/></svg><span>48 Orchard Lane, Staunton<br>24401, Virginia</span></div>
  <div class="contact-line" style="top:184px"><svg width="14" height="16" viewBox="0 0 14 16"><path d="M2 1 L5 1 L6 5 L4 6 C5 9 7 11 10 12 L11 10 L14 11 L14 14 C8 15 0 8 2 1Z" fill="#3f9a1e"/></svg><span>(540) 555-0142</span></div>
  <div class="contact-line" style="top:214px"><svg width="15" height="12" viewBox="0 0 15 12"><rect x="0" y="0" width="15" height="12" fill="#3f9a1e"/><path d="M0 0 L7.5 6 L15 0" stroke="#0d0d0d" stroke-width="1.5" fill="none"/></svg><span>hello@thequillmarkfarms.com</span></div>

  <div class="foot-col" style="left:493px"><h6>Information</h6><a>About Us</a><a>Why Choose Us</a><a>Our Products</a><a>What People Says</a><a>Contact Us</a></div>
  <div class="foot-col" style="left:690px"><h6>Sitemap</h6><a>Our Blogs</a><a>Hemp Products</a><a>CBD Products</a><a>Term of Use</a><a>Contact Us</a></div>
  <div class="foot-col" style="left:874px"><h6>Join Our Newsletters</h6></div>
  <div class="newsletter-input">Your Email address</div>
  <a class="btn btn-tan">Subscribe &rsaquo;</a>
  <span class="social" style="left:880px"></span>
  <span class="social" style="left:918px"></span>
  <span class="social" style="left:956px"></span>
  <span class="social" style="left:994px"></span>

  <div class="foot-rule"></div>
  <div class="copyright" style="left:104px">© Copyright 2020 . Quillmark Farms . All Right Reserved</div>
  <div class="copyright" style="left:947px">Terms &amp; Conditions &nbsp;|&nbsp; Privacy Policy</div>
</footer>

</body>
</html>
```